Leading the way in online fitness and education requires power house web design

If you need to contact me you can do so via
skype: Travlin

We need a website designed for new company based in Houston Texas called "TravlinFit". We offer web based training and nutrition programs for our members for example we use the same software as these companies: http://marobelka.com/ http://www.liftquorra.com/ i would like my visitors to be captivated by the level of design creativity of the site.

colors to use would be grey, orange and green.
for example i like the green of this site http://www.cartbeam.com/
i will upload my logo files so you can get a feel for shades of grey and orange.

there is a 3d effect filter i would like applied to my logo for use in the web design i have uploaded what that effect looks like.

i will need your designs to be complete with all interior pages which will include Home, Fitness, Nutrition, Fit Lounge, Fit Score, Fit School, Contact Us, Sign up.

fit lounge on my site is the same as pathwick on liftquorra and locker room on marobelka just re branded.

fit school is a research corner for members to learn about health and fitness, we are members of major medical journals on health and fitness and will have all our articles be from the newest research findings.

competitor sites
these sites use same software:
http://marobelka.com/
http://www.liftquorra.com/

these sites are other software.
http://home.sprintmesa.com/software-for-athletes.aspx
http://www.vigordex.com/

here are some websites that i like:
http://www.crestwaveplay.com/
http://www.nub-lantern.com/
http://fimzol.com/
http://www.parqudo.com/
http://www.lortavi.de/fandiloop/
http://brisketmade.com/

i also like the greens in this site that i am uploading

I have been reviewing the designs and would like to update everyone at once I do not want a normal fitness website design style, no testimonials, blog post, bodyfat calculator

my website will be a membership based website. i want the website to sell the main points of my fitness app that my members will have access to look at the comments for my selling points, use those points in the site create designs and graphics to visualize those points.

look at these sites and gain inspiration

http://www.tuvelo.com.pl/#/projekty/case-studies
http://www.quendar.com/en#/home#ld-kpvm-402617-0045
http://www.nub-lantern.com/
http://fimzol.com/
http://www.parqudo.com/

i have a few designers asking me what the selling points are, the website needs to be built around these points

main selling points.

overview

programs utilize the best multi-joint exercises combined with high intensity cardio, to give you a full-body workout, efficiently and effectively. This means you’re burning more calories and building more lean muscle per unit of time than traditional weight training and cardio programs.

When you sign up, you''ll receive a work out and diet plan to fit your goals and fitness level. As you progress through your plan, you can use the personal fitness and meal calendar to record your results. When you sign-up we''ll ask you a series of questions and your workouts will be tailored to your exact needs. That means never having to use a generic diet and exercise plan again.

If you''ve ever tried to lose weight and build muscle and didn''t succeed, we feel your pain. Until now, trying to navigate all the fitness fads and latest trends on your own has been difficult. The best option - hiring a certified personal trainer - may be out of your financial reach. That''s where we come in - we''re personal trainers on a mission to help you reach your fitness goals quickly and for less money than in person training. Best of all, we''re here to help you day or night.

Fitness

Personal Fitness Calendar

Tailored to the member’s schedule and flexible to accommodate any changes to a member’s regular fitness schedule. Track your progress and stay on track with your fitness goals.

Custom Fitness Plan

Based on a member’s current physical condition and goals.

• Step by step exercise instructions
• 3-D video demonstrations of over 600 exercises, including functional and body-weight only movements
• Equipment filter can customize plans to your gym’s equipment package
• Record workouts to track exercise history and progression

Nutrition

Nutritional Assessment

Daily recommended caloric intake (Protein, Carbohydrates and Fats), based on personal profile and daily fitness plan.

Custom Meal Plan

Personalized meal plan based on nutritional assessment.

• Choose number of meals per day
• Add dietary restrictions, food preferences or dislikes
• Database of thousands of ingredients allows for hundreds of thousands of meal combinations
• Include favorite foods by entering custom nutritional information

Weight tracking

Calculate goal weight and track weight-loss or weight-gain progress. You will reach your goals in no time.

Fit Lounge

What is the most important part of any workout or fitness program? Staying motivated. And what better form of motivation than positive encouragement from your peers?

Fit Lounge is fitness focused social network for health-minded individuals looking for a simple and convenient place to track their workout goals and monitor their progress. A unique system of motivation, support and accountability makes setting fitness goals and then keeping up with them easy

Track

Start by setting fitness goals that you want to track. They can be anything from running and jogging to how many hours of sleep you are getting and how many glasses of water you are drinking every day. Other members of the travlinfits community might be tracking the same workout goals as you, so you can always join their groups as well.

Share

Once you start tracking your workout goals, you can share your progress with your friends. Reach a new max on your bench press? Let everyone know. Eclipse the 10 mile mark on your daily run? Spread the word! The communication of encouragement back and forth is a great way to ensure that everyone stays on track with their workout goals.

Achieve

Of course, the point of any workout or fitness program is to achieve the goals you’ve set. And with help from travlinfits workout tracking tools and encouragement from the community, you will achieve your workout goals in no time. When you see a friend has achieved his or her fitness goals, you can send them a virtual “fist bump” as a sign of congratulations. The number of “fist bumps” each user accumulates will be displayed on their profile, providing additional motivation and a healthy dose of competition.

Reason: i dont feel the designs i have received are of the quality i am looking for

check this website out, i know its flash, but i also know you can get creative without flash and have nice effects throughout the site.

http://www.driftlane-hub.com/

I dont want plain jane designs, insert the content i provided into the site and have it explored in a unique way. take as much time on the design as you need as i will keep extending deadline until i find one that is perfect.

as said before don't make the site anything like the competition sites, its only purpose is to sell the memberships using content provided so i need an innovative way to for them to explore that content,

as your designing this site add me on skype so i can detail and help brainstorm ideas my skype id is travlin
you can stray from the color scheme a little or throw it away if you want i just want to see how creative you can get.

Industry/Entity Type

School

Requirements
Nice to have
• if you notice at the bottom of http://marobelka.com/ she has the orange bar with the three short content parts, i like the idea of having a space like that for similar content.

on http://www.vigordex.com/ if you look to the left side of the scrolling icons i like the idea of having icons or animated pictures to point of key benefits.

```html
<!DOCTYPE html>
<html lang="en">
<head>
<meta charset="utf-8">
<title>TravlinFit — Your Personal Online Training Solution</title>
<link rel="stylesheet" href="https://fonts.googleapis.com/css2?family=Open+Sans:ital,wght@0,400;0,600;0,700;1,400&display=swap">
<style>
  :root {
    --bar-dark: #262626;
    --bar-darker: #1c1c1c;
    --green-deep: #4f8f16;
    --green-mid: #7cbd2a;
    --green-light: #a5d84a;
    --glow: #e6ffc4;
    --white: #ffffff;
    --ink: #2f3a22;
    --muted: #9a9a9a;
    --orange: #f0801e;
  }
  * { margin: 0; padding: 0; box-sizing: border-box; }
  html, body { width: 1200px; height: 717px; overflow: hidden; background: var(--bar-darker); }
  body { font-family: "Open Sans", Arial, sans-serif; position: relative; }

  .site-header {
    position: absolute; left: 0; top: 0; width: 1200px; height: 130px;
    background: linear-gradient(180deg, #2d2d2d, var(--bar-dark));
    border-bottom: 1px solid #3c4a2b;
  }
  .brand {
    position: absolute; left: 132px; top: 48px;
    display: flex; align-items: center; gap: 12px;
    font-size: 40px; font-weight: 700; color: var(--white); letter-spacing: -0.5px;
  }
  .brand-mark { width: 28px; height: 28px; border-radius: 50%; background: var(--orange); }
  .utility-nav {
    position: absolute; right: 132px; top: 11px; display: flex; gap: 17px;
    font-size: 11.5px; color: #c9c9c9;
  }
  .utility-nav span { display: flex; align-items: center; gap: 5px; }
  .utility-nav svg { width: 13px; height: 13px; fill: #bdbdbd; }
  .social { position: absolute; top: 60px; display: flex; flex-direction: column; align-items: center; gap: 4px; }
  .social-label { font-size: 10px; font-weight: 700; color: #8a8a8a; }
  .social-box { width: 40px; height: 40px; border-radius: 5px; background: #4a4a4a; opacity: .8; }
  .social.chirper { left: 958px; }
  .social.palbook { left: 1021px; }

  .hero {
    position: absolute; left: 0; top: 130px; width: 1200px; height: 518px;
    background:
      radial-gradient(ellipse 420px 360px at 890px 300px, rgba(230,255,196,.55), transparent 70%),
      radial-gradient(ellipse 700px 400px at 300px 250px, var(--green-light), transparent 80%),
      linear-gradient(180deg, var(--green-mid), var(--green-deep));
    overflow: hidden;
  }
  .download-btn {
    position: absolute; left: 986px; top: 14px; width: 82px; height: 50px;
    border-radius: 4px; background: rgba(255,255,255,.12);
    display: flex; align-items: center; justify-content: center;
  }
  .welcome { position: absolute; left: 130px; top: 73px; font-size: 28px; font-style: italic; color: var(--ink); }
  .headline {
    position: absolute; left: 128px; top: 108px; font-size: 58px; font-weight: 700;
    line-height: 72px; color: var(--white); letter-spacing: 1px;
  }
  .intro { position: absolute; left: 130px; top: 258px; width: 490px; font-size: 17.5px; line-height: 22px; color: var(--white); }
  .intro p + p { margin-top: 10px; }
  .trainers-photo {
    position: absolute; left: 690px; top: 20px; width: 400px; height: 498px;
    background: radial-gradient(ellipse at 50% 55%, rgba(255,255,255,.75), rgba(240,250,225,.35) 55%, transparent 75%);
  }

  .section-nav { position: absolute; left: 132px; top: 442px; display: flex; gap: 4px; }
  .nav-tab {
    width: 82px; height: 56px; border-radius: 4px;
    background: rgba(255,255,255,.12); border: 1px solid rgba(255,255,255,.1);
    display: flex; align-items: center; justify-content: center;
  }
  .nav-tab svg { width: 40px; height: 36px; fill: rgba(255,255,255,.18); }
  .nav-tab.is-active {
    background: linear-gradient(180deg, #8fd13a, #4f9a12); border-color: #b8ec78;
    flex-direction: column; justify-content: flex-end; padding-bottom: 6px; position: relative;
  }
  .nav-tab.is-active svg { position: absolute; top: -22px; width: 54px; height: 44px; fill: var(--white); }
  .nav-label { font-size: 13px; font-weight: 700; color: var(--white); }

  .site-footer {
    position: absolute; left: 0; top: 648px; width: 1200px; height: 69px;
    background: linear-gradient(180deg, #2b2b2b, var(--bar-darker));
    border-top: 1px solid #6a8f3a;
  }
  .copyright { position: absolute; left: 130px; top: 13px; font-size: 12px; color: var(--muted); }
</style>
</head>
<body>
  <header class="site-header">
    <div class="brand"><span class="brand-mark"></span>TravlinFit</div>
    <nav class="utility-nav">
      <span><svg viewBox="0 0 12 12"><path d="M3 0h6v12L6 9 3 12z"/></svg>Bookmark</span>
      <span><svg viewBox="0 0 12 12"><path d="M0 1h12v8H4l-3 3V9H0z"/></svg>Contact</span>
      <span><svg viewBox="0 0 12 12"><circle cx="6" cy="6" r="4.5"/><circle cx="6" cy="6" r="1.8" fill="#2b2b2b"/></svg>Register</span>
      <span><svg viewBox="0 0 12 12"><circle cx="8" cy="4" r="3.5"/><path d="M6 5L0 11l1 1 2-2 1 1 1-1-1-1 3-3z"/></svg>Login</span>
    </nav>
    <div class="social chirper"><span class="social-label">CHIRPER</span><span class="social-box"></span></div>
    <div class="social palbook"><span class="social-label">PALBOOK</span><span class="social-box"></span></div>
  </header>

  <main class="hero">
    <div class="trainers-photo" role="img" aria-label="Three smiling personal trainers framed by a soft green glow"></div>
    <div class="download-btn">
      <svg width="46" height="46" viewBox="0 0 46 46"><circle cx="23" cy="23" r="20" fill="none" stroke="rgba(255,255,255,.35)" stroke-width="3"/><path d="M18 11h10v12h6L23 35 12 23h6z" fill="rgba(255,255,255,.35)"/></svg>
    </div>
    <p class="welcome">Welcome to Travlin Fit:</p>
    <h1 class="headline">REACH YOUR<br>GOALS QUICKLY.</h1>
    <div class="intro">
      <p>We're personal trainers on a mission to help you reach your fitness goals quickly and for less money.</p>
      <p>Best of all, we're here to help you day or night.</p>
    </div>
    <nav class="section-nav">
      <div class="nav-tab is-active">
        <svg viewBox="0 0 54 44"><path d="M27 2L2 22h7v20h13V30h10v12h13V22h7z"/></svg>
        <span class="nav-label">HOME</span>
      </div>
      <div class="nav-tab"><svg viewBox="0 0 40 36"><rect x="2" y="8" width="36" height="3"/><rect x="3" y="4" width="4" height="11"/><rect x="33" y="4" width="4" height="11"/><circle cx="20" cy="6" r="4"/><rect x="15" y="12" width="10" height="12"/><rect x="15" y="24" width="4" height="12"/><rect x="21" y="24" width="4" height="12"/></svg></div>
      <div class="nav-tab"><svg viewBox="0 0 40 36"><path d="M20 8c-6-4-15-1-14 10s7 18 14 16c7 2 13-5 14-16S26 4 20 8z"/><rect x="19" y="1" width="2" height="7"/></svg></div>
      <div class="nav-tab"><svg viewBox="0 0 40 36"><circle cx="20" cy="18" r="15" fill="none" stroke="rgba(255,255,255,.18)" stroke-width="4" stroke-dasharray="10 4"/><circle cx="20" cy="18" r="9"/></svg></div>
      <div class="nav-tab"><svg viewBox="0 0 40 36"><rect x="4" y="4" width="24" height="18"/><rect x="4" y="24" width="32" height="6"/><rect x="30" y="10" width="6" height="14"/><rect x="6" y="30" width="4" height="6"/><rect x="30" y="30" width="4" height="6"/></svg></div>
      <div class="nav-tab"><svg viewBox="0 0 40 36"><rect x="14" y="2" width="24" height="18" fill="none" stroke="rgba(255,255,255,.18)" stroke-width="3"/><circle cx="8" cy="10" r="4"/><path d="M2 36V18h12l8-4 1 3-9 5v14z"/></svg></div>
      <div class="nav-tab"><svg viewBox="0 0 40 36"><path d="M2 6h36v24H2z"/><path d="M2 6l18 14L38 6" fill="none" stroke="rgba(0,0,0,.15)" stroke-width="2"/></svg></div>
    </nav>
  </main>

  <footer class="site-footer">
    <p class="copyright">© 2012 All Rights Reserved. TravlinFit</p>
  </footer>
</body>
</html>
```